New Website for Consulting Company

Our company needs a fresh web design to help us drive our business forward. We are a consulting and software provider to Airports, Air Traffic Organizations, Builders and Architects. We specialize in analyzing operations, monitoring noise levels and creating software to improve operations, meet customer requirements and improve public relations.
Additional Info:
- Additional requirements can be found in the Web Design Brief
- Logo and logo branding attached
Target Market(s)
Airlines, Airports, Government Agencies, and Real Estate Developers
Industry/Entity Type
Aviation
Coding
Coded - Design and coding required
Number of Pages Required
2 page
Colors
Designer to choose colors to be used in the design.
Requirements
Must have
- - Create a Wordpress Design (Coded - Design and coding required)
- - Designer must provide full implementation/coding depending on the platform chosen by the client (i.e. Wordpress theme, HTML/CSS, etc.)
- - This is a multi-page site; Supporting pages can be formatted the same, but links need to be in place
- - Colors used must be grey scale, black or match the logo. It is not necessary to use all the colors in our logo
Should not have
- We are not looking for an overly bright site. While our logo has 5 different colors, it is not necessary to use all of them.

```html
<!DOCTYPE html>
<html lang="en">
<head>
<meta charset="utf-8">
<title>SkyLattice International</title>
<link rel="stylesheet" href="https://fonts.googleapis.com/css2?family=Montserrat:wght@400;500;600;700&family=Open+Sans:wght@400;600&display=swap">
<style>
:root{
  --blue:#2b71b6;
  --blue-dark:#1f5c98;
  --hero-a:#3f78ad;
  --hero-b:#1f4f82;
  --ink:#222b35;
  --muted:#6c7480;
  --light:#f3f4f6;
  --line:#e3e6ea;
  --footer:#1b2430;
  --accent:#f0a43a;
  --white:#fff;
}
*{margin:0;padding:0;box-sizing:border-box}
html,body{width:1200px;height:3005px;overflow:hidden}
body{position:relative;font-family:"Open Sans",Arial,sans-serif;color:var(--ink);background:var(--white)}
.abs{position:absolute}
h1,h2,h3,.nav,.btn,.brand{font-family:"Montserrat",Arial,sans-serif}

/* hero */
.hero{left:0;top:0;width:1200px;height:442px;background:linear-gradient(160deg,var(--hero-a),var(--hero-b))}
.hero-photo{left:0;top:0;width:1200px;height:442px;background:linear-gradient(180deg,rgba(120,160,200,.35),rgba(40,70,110,.35))}
.brand{left:186px;top:34px;color:var(--white);font-size:26px;font-weight:700;display:flex;align-items:center;gap:8px}
.brand .dot{width:14px;height:14px;background:var(--white);border-radius:50%}
.topbar{left:638px;top:30px;color:var(--white);font-size:13px;display:flex;gap:36px}
.topbar .phone{font-size:17px}
.topbar span{display:flex;align-items:center;gap:8px}
.nav{left:456px;top:62px;display:flex;gap:26px;color:var(--white);font-size:12px}
.nav a{color:inherit;text-decoration:none;padding-bottom:4px}
.nav a.active{border-bottom:2px solid var(--white)}
.hero-kicker{left:186px;top:182px;color:var(--white);font-size:16px;padding-bottom:10px}
.hero-kicker::after{content:"";position:absolute;left:0;bottom:0;width:56px;height:2px;background:#7cc142}
.hero-title{left:186px;top:224px;color:var(--white);font-size:22px;font-weight:600;line-height:32px}
.btn{display:inline-block;font-size:11px;text-decoration:none;color:var(--white)}
.btn-outline{border:1px solid var(--white);padding:8px 18px}
.hero .btn{left:186px;top:306px}
.dots{left:186px;top:366px;display:flex;gap:8px}
.dots i{width:8px;height:8px;border-radius:50%;background:rgba(255,255,255,.5)}
.dots i:first-child{background:var(--white)}
.monitor{left:622px;top:136px;width:278px;height:348px;background:linear-gradient(180deg,#f6f7f9 0,#eef0f3 70%,#c9ccd1 100%);border-radius:6px}

/* offer */
.offer-shot{left:204px;top:534px;width:386px;height:384px;background:linear-gradient(90deg,#2d3a4a 0 58px,#f7f8fa 58px);box-shadow:0 10px 30px rgba(0,0,0,.18)}
.play{left:374px;top:686px}
.offer h2{left:630px;top:570px;font-size:22px;font-weight:500;line-height:28px;color:var(--ink)}
.offer p{left:630px;width:340px;font-size:11.5px;line-height:20px;color:var(--muted)}
.btn-solid{background:var(--blue);padding:8px 18px}

/* categories */
.cats{left:0;top:1002px;width:1200px;height:432px;background:var(--light)}
.sec-title{width:1200px;text-align:center;font-size:22px;font-weight:500;left:0}
.sec-sub{width:1200px;text-align:center;font-size:11.5px;color:var(--muted);left:0}
.sec-rule{left:570px;width:60px;height:2px;background:var(--blue)}
.cat{width:180px;text-align:center}
.cat .ring{width:88px;height:88px;margin:0 auto;border:1.5px solid var(--blue);border-radius:50%;display:flex;align-items:center;justify-content:center}
.cat h3{margin-top:26px;font-size:14px;font-weight:600}
.cat p{margin-top:8px;font-size:11px;line-height:20px;color:var(--muted)}
.more{display:inline-block;margin-top:6px;font-size:11px;color:var(--blue);text-decoration:none}

/* airspace */
.air{left:0;top:1434px;width:596px;height:460px;background:linear-gradient(135deg,#2f7dc2,#1d5d9c);color:var(--white)}
.air h2{position:absolute;left:208px;top:50px;font-size:24px;font-weight:500}
.air .sub{position:absolute;left:208px;top:88px;font-size:11px}
.air .rule{position:absolute;left:208px;top:106px;width:40px;height:2px;background:var(--white)}
.air p{position:absolute;left:208px;width:356px;font-size:11.5px;line-height:20px}
.air .btn{position:absolute;left:208px;top:374px}
.air-scene{left:596px;top:1434px;width:604px;height:460px;background:linear-gradient(160deg,#4a3b55,#2a2436 60%,#3b2f3e)}

/* blog */
.card{width:250px;height:404px;background:var(--white);box-shadow:0 2px 10px rgba(0,0,0,.08)}
.card .photo{height:192px;background:linear-gradient(160deg,#d8d4cf,#a8a29a)}
.card .body{padding:16px 22px}
.card h3{font-size:11.5px;font-weight:700;line-height:20px}
.card .meta{margin-top:6px;font-size:10px;color:var(--accent)}
.card p{margin-top:8px;font-size:11px;line-height:20px;color:var(--muted)}
.card .more{margin-top:12px}

/* footer */
.footer{left:0;top:2504px;width:1200px;height:501px;background:linear-gradient(160deg,#2a3442,#151c26)}
.footer *{color:var(--white)}
.fcol{width:266px;text-align:center;font-size:11.5px;line-height:18px}
.fcol svg{display:block;margin:0 auto 18px}
.vline{width:0;height:130px;border-left:1px dashed rgba(255,255,255,.45);top:2652px}
.cities{left:0;width:1200px;top:2834px;text-align:center;font-size:11px;word-spacing:4px}
.copy{left:0;width:1200px;top:2862px;text-align:center;font-size:11px}
.social{left:572px;top:2914px;display:flex;gap:10px}
.social i{width:24px;height:24px;border:1px solid rgba(255,255,255,.7);border-radius:50%}
</style>
</head>
<body>

<header class="abs hero">
  <div class="abs hero-photo" role="img" aria-label="Airport runway with a passenger jet under a blue sky"></div>
  <div class="abs brand"><span class="dot"></span>SkyLattice</div>
  <div class="abs topbar">
    <span><svg width="12" height="9" viewBox="0 0 12 9"><rect x=".5" y=".5" width="11" height="8" fill="none" stroke="#fff"/><path d="M.5 .5 6 5l5.5-4.5" fill="none" stroke="#fff"/></svg>info@skylattice-example.com</span>
    <span class="phone"><svg width="13" height="13" viewBox="0 0 24 24"><path fill="#fff" d="M6.6 10.8a15 15 0 0 0 6.6 6.6l2.2-2.2c.3-.3.7-.4 1-.2 1.1.4 2.3.6 3.6.6.6 0 1 .4 1 1V20c0 .6-.4 1-1 1A17 17 0 0 1 3 4c0-.6.4-1 1-1h3.5c.6 0 1 .4 1 1 0 1.3.2 2.5.6 3.6.1.3 0 .7-.2 1z"/></svg>+1 (555) 010-1222</span>
  </div>
  <nav class="abs nav">
    <a class="active" href="#">Home</a><a href="#">Airports</a><a href="#">Airspace</a><a href="#">Emissions coustics</a><a href="#">Visualization</a><a href="#">About</a><a href="#">Contact</a>
  </nav>
  <p class="abs hero-kicker">SkyLattice International Provide software to</p>
  <h1 class="abs hero-title">Airports, Air Traffic Organizations,<br>Builders and Architects</h1>
  <a class="abs btn btn-outline" href="#">Explore More &#10141;</a>
  <div class="abs dots"><i></i><i></i><i></i></div>
  <div class="abs monitor" role="img" aria-label="Desktop monitor showing the analytics dashboard"></div>
</header>

<section class="offer">
  <div class="abs offer-shot" role="img" aria-label="Software dashboard screenshot with noise level line charts"></div>
  <svg class="abs play" width="46" height="46" viewBox="0 0 46 46"><circle cx="23" cy="23" r="23" fill="#c9302c"/><path d="M18 14v18l14-9z" fill="#fff"/></svg>
  <h2 class="abs">We offer&nbsp; software updates,<br>training and support</h2>
  <p class="abs" style="top:648px">SkyLattice International invents and deploys innovative management and technology solutions that address complex noise and airspace issues for airports and residential communities.</p>
  <p class="abs" style="top:746px">With more than two decades of experience and original software solutions, the company identifies problems precisely and solves them through a diagnostic.</p>
  <a class="abs btn btn-solid" style="left:630px;top:832px" href="#">Get Started Now</a>
</section>

<section class="abs cats"></section>
<h2 class="abs sec-title" style="top:1056px">Primary Categories</h2>
<p class="abs sec-sub" style="top:1086px">We have 4 primary categories of operations</p>
<div class="abs sec-rule" style="top:1110px"></div>

<div class="abs cat" style="left:208px;top:1148px">
  <div class="ring"><svg width="34" height="34" viewBox="0 0 24 24"><path fill="#2b71b6" d="M21 16v-2l-8-5V3.5a1.5 1.5 0 0 0-3 0V9l-8 5v2l8-2.5V19l-2 1.5V22l3.5-1 3.5 1v-1.5L13 19v-5.5z" transform="rotate(45 12 12)"/></svg></div>
  <h3>Airports</h3><p>For over 20 years, SkyLattice International has been an aviation consulting....</p><a class="more" href="#">Read More &#10141;</a>
</div>
<div class="abs cat" style="left:406px;top:1148px">
  <div class="ring"><svg width="34" height="34" viewBox="0 0 24 24" fill="none" stroke="#2b71b6" stroke-width="1.5"><rect x="3" y="4" width="18" height="15" rx="1"/><path d="M3 8h18"/><circle cx="12" cy="13.5" r="3"/></svg></div>
  <h3>Software</h3><p>Lorem Ipsum is simply dummy text of the printing and typesetting industry.....</p><a class="more" href="#">Read More &#10141;</a>
</div>
<div class="abs cat" style="left:602px;top:1148px">
  <div class="ring"><svg width="34" height="34" viewBox="0 0 24 24" fill="none" stroke="#2b71b6" stroke-width="1.5"><path d="M3 10h4l8-5v14l-8-5H3z"/><path d="M18 9c1.5 1.5 1.5 4.5 0 6M20 7c2.5 2.5 2.5 7.5 0 10"/></svg></div>
  <h3>Noise &amp; Emissions</h3><p>Lorem Ipsum is simply dummy text of the printing and typesetting industry.....</p><a class="more" href="#">Read More &#10141;</a>
</div>
<div class="abs cat" style="left:810px;top:1148px">
  <div class="ring"><svg width="34" height="34" viewBox="0 0 24 24" fill="none" stroke="#2b71b6" stroke-width="1.5"><circle cx="12" cy="12" r="9"/><circle cx="12" cy="12" r="4"/><path d="M5 12c2-3 12-3 14 0c-2 3-12 3-14 0z"/></svg></div>
  <h3>Visualization</h3><p>Lorem Ipsum is simply dummy text of the printing and typesetting industry.....</p><a class="more" href="#">Read More &#10141;</a>
</div>

<section class="abs air">
  <h2>Airspace</h2>
  <span class="sub">Lorem Ipsum is simply dummy text of the printing</span>
  <span class="rule"></span>
  <p style="top:130px">SkyLattice International provides airspace visualization services to airports, governments, and partner corporations throughout the world. Airspace visualization services encompass SkyLattice's innovative approach to graphically show what airspace looks like, and how aircraft fly within the confines of assigned airspace.</p>
  <p style="top:262px">Visualizing what has traditionally been shown in 2D into 3D brings into focus how technology changes can greatly benefit the entire airspace system. Our airspace visualization services are able.</p>
  <a class="btn btn-outline" href="#">Explore More &#10141;</a>
</section>
<div class="abs air-scene" role="img" aria-label="Isometric 3D illustration of an airport terminal, gates and taxiway at night"></div>

<h2 class="abs sec-title" style="top:1944px">Blog</h2>
<p class="abs sec-sub" style="top:1976px">Lorem Ipsum is simply dummy text of the printing.</p>

<article class="abs card" style="left:206px;top:2040px">
  <div class="photo" role="img" aria-label="Photo of a woman holding a tablet"></div>
  <div class="body"><h3>Lorem Ipsum is simply dummy text of the printing</h3><p class="meta">March 8, 2016 &nbsp;0 Comments</p><p>Lorem ipsum dolor sit amet, consectetuer adipiscing elit, sed diam nonummy nibh dolor sit kd-tamet, consectetuer.....</p><a class="more" href="#">Read More &#10141;</a></div>
</article>
<article class="abs card" style="left:474px;top:2040px">
  <div class="photo" role="img" aria-label="Photo of a man holding a tablet in an office"></div>
  <div class="body"><h3>Lorem Ipsum is simply dummy text of the printing</h3><p class="meta">March 8, 2016 &nbsp;0 Comments</p><p>Lorem ipsum dolor sit amet, consectetuer adipiscing elit, sed diam nonummy nibh dolor sit kd-tamet, consectetuer.....</p><a class="more" href="#">Read More &#10141;</a></div>
</article>
<article class="abs card" style="left:742px;top:2040px">
  <div class="photo" role="img" aria-label="Photo of a businessman seated using a tablet"></div>
  <div class="body"><h3>Lorem Ipsum is simply dummy text of the printing</h3><p class="meta">March 8, 2016 &nbsp;0 Comments</p><p>Lorem ipsum dolor sit amet, consectetuer adipiscing elit, sed diam nonummy nibh dolor sit kd-tamet, consectetuer.....</p><a class="more" href="#">Read More &#10141;</a></div>
</article>

<footer class="abs footer" role="img" aria-label="Dimmed isometric city illustration behind the contact details"></footer>
<h2 class="abs sec-title" style="top:2556px;color:#fff">Contact Us</h2>
<p class="abs sec-sub" style="top:2588px;color:#fff">Lorem Ipsum is simply dummy text of the printing.</p>

<div class="abs fcol" style="left:200px;top:2664px;color:#fff">
  <svg width="30" height="30" viewBox="0 0 24 24"><path fill="none" stroke="#fff" stroke-width="1.3" d="M6.6 10.8a15 15 0 0 0 6.6 6.6l2.2-2.2c.3-.3.7-.4 1-.2 1.1.4 2.3.6 3.6.6.6 0 1 .4 1 1V20c0 .6-.4 1-1 1A17 17 0 0 1 3 4c0-.6.4-1 1-1h3.5c.6 0 1 .4 1 1 0 1.3.2 2.5.6 3.6.1.3 0 .7-.2 1z"/></svg>
  <span style="color:#fff">Call: +1 (555) 010-1222<br>FAx: +1 (555) 010-1225</span>
</div>
<div class="abs vline" style="left:466px"></div>
<div class="abs fcol" style="left:466px;top:2664px">
  <svg width="30" height="30" viewBox="0 0 24 24" fill="none" stroke="#fff" stroke-width="1.3"><path d="M12 22s7-7 7-12a7 7 0 0 0-14 0c0 5 7 12 7 12z"/><circle cx="12" cy="10" r="2.5"/></svg>
  <span style="color:#fff"><b>Bayview Office:</b><br>4100 Harbor Lane, Suite 250<br>Bayview, CA 90000</span>
</div>
<div class="abs vline" style="left:732px"></div>
<div class="abs fcol" style="left:732px;top:2664px">
  <svg width="32" height="30" viewBox="0 0 24 20" fill="none" stroke="#fff" stroke-width="1.3"><rect x="1" y="2" width="22" height="16"/><path d="M1 2l11 9 11-9"/></svg>
  <span style="color:#fff">E-mail Us<br><u>info@skylattice-example.com</u></span>
</div>

<p class="abs cities" style="color:#fff">Bayview &nbsp;/&nbsp; San Diego &nbsp;/&nbsp; Georgetown</p>
<p class="abs copy" style="color:#fff">Copyright &copy; 2017 SkyLattice</p>
<div class="abs social"><i></i><i></i></div>

</body>
</html>
```